San Francisco Pet Care Non Profit

Business Card Design for non profit organization.
We are a mobile pet care team who supports and attends to pets whose owners are homeless. Thanks for your help and creativity.

Industry/Entity Type

Non Profit

Contact Information for Business Card

Miriam Loxley
President
2817 Harrow Street, #516
San Francisco, CA 94187
phone: 415-782-3946
fax: 415-718-4053
miriam@warmpawvan.org
website: warmpawvan.org
facebook: facebook.com/WarmPawVan

Font styles to use
Serif
Sans Serif

Colors

Designer to choose colors to be used in the design.

Requirements
Must have
• above details and attached logo

```html
<!DOCTYPE html>
<html lang="en">
<head>
<meta charset="utf-8">
<title>WarmPawVan Business Card</title>
<link href="https://fonts.googleapis.com/css2?family=Arimo:wght@400;700&display=swap" rel="stylesheet">
<style>
  :root {
    --backdrop: #e4e4e4;
    --card-light: #ffffff;
    --card-dark: #231f20;
    --brand-blue: #0ba5e7;
    --rule-blue: #1a74b0;
    --ink: #333333;
    --ink-soft: #4a4a4a;
    --white: #ffffff;
  }
  * { margin: 0; padding: 0; box-sizing: border-box; }
  html, body {
    width: 1125px;
    height: 1200px;
    overflow: hidden;
    background: var(--backdrop);
    font-family: "Arimo", Arial, sans-serif;
  }
  .canvas {
    position: relative;
    width: 1125px;
    height: 1200px;
  }
  .card {
    position: absolute;
    left: 150px;
    width: 826px;
    height: 472px;
  }
  .card-front {
    top: 98px;
    background: var(--card-light);
  }
  .card-back {
    top: 631px;
    background: var(--card-dark);
  }
  .person-name {
    position: absolute;
    left: 61px;
    top: 50px;
    font-size: 31px;
    font-weight: 700;
    color: var(--brand-blue);
  }
  .person-title {
    position: absolute;
    left: 62px;
    top: 84px;
    font-size: 20px;
    font-weight: 700;
    color: var(--ink);
  }
  .title-rule {
    position: absolute;
    left: 65px;
    top: 135px;
    width: 63px;
    height: 2px;
    background: var(--rule-blue);
  }
  .contact-list {
    position: absolute;
    left: 65px;
    top: 186px;
    list-style: none;
    font-size: 19px;
    line-height: 29px;
    color: var(--ink-soft);
  }
  .contact-list b { color: var(--ink); }
  .address {
    position: absolute;
    left: 62px;
    top: 368px;
    font-size: 19.5px;
    line-height: 25px;
    color: var(--ink-soft);
    font-style: normal;
  }
  .front-brand {
    position: absolute;
    left: 560px;
    top: 215px;
    width: 210px;
    display: flex;
    flex-direction: column;
    align-items: center;
    gap: 14px;
  }
  .brand-dot {
    width: 96px;
    height: 96px;
    border-radius: 50%;
    background: var(--brand-blue);
  }
  .front-brand .brand-name {
    font-size: 28px;
    font-weight: 700;
    color: var(--brand-blue);
  }
  .back-lockup {
    position: absolute;
    left: 0;
    right: 0;
    top: 180px;
    display: flex;
    align-items: center;
    justify-content: center;
    gap: 24px;
  }
  .back-lockup .brand-dot {
    width: 82px;
    height: 82px;
  }
  .back-text {
    display: flex;
    flex-direction: column;
    align-items: center;
  }
  .back-text .brand-name {
    font-size: 62px;
    font-weight: 700;
    color: var(--brand-blue);
    line-height: 1;
  }
  .tagline {
    margin-top: 6px;
    font-size: 24px;
    font-weight: 700;
    color: var(--white);
  }
</style>
</head>
<body>
<main class="canvas">
  <section class="card card-front">
    <h1 class="person-name">Miriam Loxley</h1>
    <p class="person-title">President</p>
    <div class="title-rule"></div>
    <ul class="contact-list">
      <li><b>P:</b> 415-782-3946</li>
      <li><b>C:</b> 415-718-4053</li>
      <li><b>E:</b> miriam@warmpawvan.org</li>
      <li><b>W:</b> www.warmpawvan.org</li>
      <li><b>FB:</b> /WarmPawVan</li>
    </ul>
    <address class="address">2817 Harrow Street, #516<br>San Francisco, CA 94187</address>
    <div class="front-brand">
      <span class="brand-dot"></span>
      <span class="brand-name">WarmPawVan</span>
    </div>
  </section>

  <section class="card card-back">
    <div class="back-lockup">
      <span class="brand-dot"></span>
      <div class="back-text">
        <span class="brand-name">WarmPawVan</span>
        <span class="tagline">Mobile Pet Care Team</span>
      </div>
    </div>
  </section>
</main>
</body>
</html>
```